Silver Bloom Marisol's Cleaning Service Business Cards Project

A business card with all contact details with logo design on there (already have a logo) eye catching Logo and contact info on one side, full logo on the back, must target upper class residential and corporate companies, fitness companies, still keep it on the feminine side of things , must look elegant

Target Market(s)

Upper class homes and corporate companies

Industry/Entity Type

Cleaning Service

Contact Information for Business Card

Name: Marisol Venturo
Position: Director
ABN: 47193802564
Email: marisolssilvercleaning@fernmail.test
Number: 0417968341

Font styles to use
Decorative

Colors

Designer to choose colors to be used in the design.

Requirements
Must have
• Available Sydney Wide, contact info and logo on one side, full logo on the back
Nice to have
• Professional appearance
Should not have
• Cheap advert looking stuff

```html
<!DOCTYPE html>
<html lang="en">
<head>
<meta charset="utf-8">
<title>Silver Bloom – Business Card</title>
<link rel="stylesheet" href="https://fonts.googleapis.com/css2?family=Alegreya:wght@500&family=Lato:wght@400&display=swap">
<style>
  :root {
    --page-bg: #e9e7e4;
    --card-navy: #2c3240;
    --text-light: #ffffff;
    --silver-light: #fafafa;
    --silver-mid: #e2e2e4;
    --silver-dark: #b9babd;
    --brand-ink: #2c3240;
  }
  * { margin: 0; padding: 0; box-sizing: border-box; }
  html, body {
    width: 1200px;
    height: 900px;
    overflow: hidden;
    background: var(--page-bg);
  }
  .canvas {
    position: relative;
    width: 1200px;
    height: 900px;
  }
  .business-card {
    position: absolute;
    left: 270px;
    top: 250px;
    width: 660px;
    height: 400px;
    border-radius: 16px;
    background: var(--card-navy);
    color: var(--text-light);
    overflow: hidden;
    box-shadow: 0 12px 30px rgba(0, 0, 0, 0.18);
  }
  .holder-name {
    position: absolute;
    left: 33px;
    top: 46px;
    font-family: "Alegreya", Georgia, serif;
    font-weight: 500;
    font-size: 26px;
    letter-spacing: 0.5px;
    text-transform: uppercase;
  }
  .holder-role {
    position: absolute;
    left: 33px;
    top: 82px;
    font-family: "Lato", Arial, sans-serif;
    font-size: 17px;
  }
  .contact {
    position: absolute;
    left: 33px;
    font-family: "Lato", Arial, sans-serif;
    font-size: 18px;
    line-height: 24px;
  }
  .contact-abn { top: 255px; }
  .contact-lines { top: 310px; }
  .brand-disc {
    position: absolute;
    left: 273px;
    top: 24px;
    width: 346px;
    height: 346px;
    border-radius: 50%;
    background: radial-gradient(circle at 40% 35%, var(--silver-light) 0%, var(--silver-mid) 60%, var(--silver-dark) 100%);
    display: flex;
    flex-direction: column;
    align-items: center;
    justify-content: center;
    text-align: center;
  }
  .brand-name {
    font-family: "Alegreya", Georgia, serif;
    font-weight: 500;
    font-size: 24px;
    line-height: 32px;
    letter-spacing: 1px;
    text-transform: uppercase;
    color: var(--brand-ink);
  }
</style>
</head>
<body>
  <main class="canvas">
    <section class="business-card">
      <h1 class="holder-name">Marisol Venturo</h1>
      <p class="holder-role">Director</p>
      <p class="contact contact-abn">ABN: 47193802564</p>
      <p class="contact contact-lines">0417968341<br>marisolssilvercleaning@fernmail.test</p>
      <div class="brand-disc">
        <p class="brand-name">Silver Bloom<br>Marisol's<br>Cleaning Service</p>
      </div>
    </section>
  </main>
</body>
</html>
```